Podcast Flyer and Business Cards

I need a like a 1/3 page vertical cardstock flyer advertising my podcast and business cards. I'd like 2 sets of each... each customized to show the books each co-host has written.

Basically a design for the card and a design for the flyer - all kind of similar

Target Market(s)

Therapy clients and students

Industry/Entity Type

Entertainment Industry

Font styles to use
Sans Serif

Colors
ec1f27

Requirements
Must have
• My logo
• see our website - www.quillbendaudiohour.com
• My picture and cohost picture - must be retouched as my eyes are bloodshot.
• head size much match
• Use couple pic as top 1/4t of page on flyer.. and side by side podcast hosts on bottom. Will get you color of male cohost walter.
• on back of card 1 for Walter - must have his books
• on back of card 2 for Denise - must have her books
Nice to have
• red and black
• Walter - Author of Open Harbor, Gentle Orbit, and co-author of Rooted Kinship Household Therapy

```html
<!DOCTYPE html>
<html lang="en">
<head>
<meta charset="utf-8">
<title>Quillbend – Couples &amp; Sex Therapy Flyer</title>
<link href="https://fonts.googleapis.com/css2?family=Oswald:wght@500&family=Source+Sans+3:wght@400;600;700&display=swap" rel="stylesheet">
<style>
  :root {
    --red: #ec1f27;
    --black: #111111;
    --ink: #1c1c1c;
    --grey-light: #f4f4f4;
    --grey-mid: #d9d9d9;
    --gold: #f6b21b;
    --page: #e8e6e3;
    --white: #ffffff;
  }
  * { box-sizing: border-box; margin: 0; padding: 0; }
  html, body { width: 1200px; height: 1132px; overflow: hidden; }
  body {
    background: var(--page);
    font-family: "Source Sans 3", Arial, sans-serif;
    color: var(--ink);
    position: relative;
  }
  .flyer {
    position: absolute;
    top: 100px;
    width: 438px;
    height: 917px;
    overflow: hidden;
    background: radial-gradient(ellipse at 50% 45%, var(--white) 40%, var(--grey-mid) 100%);
  }
  .flyer--front { left: 142px; }
  .flyer--back { left: 655px; }
  .abs { position: absolute; }

  /* front */
  .couple-photo {
    left: 0; top: 0; width: 438px; height: 440px;
    background: linear-gradient(160deg, #c9c9c9 0%, #8f8f8f 45%, #4a4a4a 75%, #bdbdbd 100%);
  }
  .swoosh { left: 0; top: 280px; width: 438px; height: 200px; }
  .brand-badge {
    width: 152px; height: 152px; border-radius: 50%;
    background: var(--black); border: 4px solid var(--white);
    display: flex; align-items: center; justify-content: center;
  }
  .brand-badge--front { left: 22px; top: 262px; }
  .brand-badge--back { left: 326px; top: 733px; width: 100px; height: 100px; border-width: 3px; }
  .brand-name {
    font-family: "Oswald", Arial, sans-serif; font-weight: 500;
    color: var(--white); font-size: 25px; letter-spacing: 2px;
  }
  .brand-badge--back .brand-name { font-size: 16px; letter-spacing: 1px; }
  .title {
    font-family: "Oswald", Arial, sans-serif; font-weight: 500;
    text-transform: uppercase; text-align: center; width: 100%; left: 0;
    white-space: nowrap; letter-spacing: -0.2px; line-height: 1.2;
  }
  .title--front { top: 426px; font-size: 25px; color: #2a2a2a; }
  .title--back { top: 42px; font-size: 25px; color: var(--red); }
  .rule { height: 1px; background: #333; }
  .rule--front { left: 40px; width: 358px; top: 466px; }
  .rule--back { left: 38px; width: 362px; top: 84px; }
  .tagline { width: 100%; left: 0; text-align: center; font-size: 21px; line-height: 1.2; }
  .tagline--front { top: 470px; color: var(--ink); }
  .tagline--back { top: 90px; color: var(--red); }
  .intro {
    left: 24px; width: 390px; top: 505px;
    font-size: 13.4px; line-height: 1.22; text-align: justify;
  }
  .rank-band {
    left: 0; top: 603px; width: 438px; height: 82px;
    background: linear-gradient(180deg, #f0242c 0%, var(--red) 60%, #c8171e 100%);
    text-align: center; color: var(--white);
  }
  .stars { color: var(--gold); font-size: 20px; letter-spacing: 1px; line-height: 1; }
  .rank-band .stars { margin-top: 6px; }
  .rank-text { font-weight: 600; font-size: 15.5px; line-height: 1.25; }
  .subscribe {
    border-radius: 18px; font-weight: 700; text-align: center; letter-spacing: 0.5px;
  }
  .subscribe--front {
    left: 70px; top: 687px; width: 298px; height: 34px; line-height: 34px;
    background: var(--black); color: var(--white); font-size: 19px;
  }
  .host { width: 150px; text-align: center; top: 730px; }
  .host--denise { left: 38px; }
  .host--walter { left: 241px; }
  .host-photo {
    width: 106px; height: 106px; border-radius: 50%; margin: 0 auto;
    border: 3px solid var(--black);
  }
  .host-photo--denise { background: radial-gradient(circle at 50% 45%, #f3c9a8 0%, #e49a5d 55%, #c76e38 100%); }
  .host-photo--walter { background: radial-gradient(circle at 50% 45%, #d8b8a0 0%, #7a6456 55%, #2b2b2b 100%); }
  .host-name { font-size: 13px; margin-top: 8px; }
  .host-role { font-size: 8.5px; margin-top: 4px; color: #444; }
  .site-band {
    left: 0; bottom: 0; width: 438px; height: 31px; line-height: 31px;
    background: var(--black); color: var(--white); text-align: center; font-size: 14px;
  }

  /* back */
  .story {
    left: 24px; width: 390px; top: 136px;
    font-size: 14.4px; line-height: 16.6px; text-align: justify;
  }
  .story p + p { margin-top: 16px; }
  .topics-heading { left: 22px; top: 520px; color: var(--red); font-weight: 700; font-size: 14px; }
  .topics {
    left: 22px; top: 545px; width: 400px;
    display: grid; grid-template-columns: 212px 188px; list-style: none;
    font-size: 13.6px; line-height: 18.5px;
  }
  .topics li::before { content: "• "; color: var(--red); }
  .rank-back { left: 0; width: 100%; top: 678px; text-align: center; color: var(--red); }
  .rank-back .rank-text { margin-top: 8px; }
  .base-wave { left: 0; top: 740px; width: 438px; height: 177px; }
  .subscribe--back {
    left: 110px; top: 800px; width: 196px; height: 36px; line-height: 36px;
    background: var(--red); color: var(--white); font-size: 19px;
  }
  .platforms {
    left: 0; width: 100%; top: 850px; text-align: center;
    color: var(--red); font-weight: 600; font-size: 16.5px; line-height: 1.3;
  }
</style>
</head>
<body>

<section class="flyer flyer--front">
  <div class="abs couple-photo" role="img" aria-label="Black and white photo of a couple embracing and kissing"></div>
  <svg class="abs swoosh" viewBox="0 0 438 200" aria-hidden="true">
    <path d="M0,110 Q230,40 438,150 L438,200 L0,200 Z" fill="var(--red)"/>
    <path d="M0,122 Q230,58 438,168 L438,200 L0,200 Z" fill="#f7f7f7"/>
  </svg>
  <div class="abs brand-badge brand-badge--front"><span class="brand-name">QUILLBEND</span></div>

  <h1 class="abs title title--front">Quillbend - Couples &amp; Sex Therapy</h1>
  <div class="abs rule rule--front"></div>
  <p class="abs tagline tagline--front">Helping couples keep it hot!</p>
  <p class="abs intro">An expert, frank and fascinating podcast about love and sex! Join us as we discuss relationship dynamics, therapy, heathy couples, marriage and family! Two international therapists bring you sound, concrete tools to find emotional connection and sexual eroticism. Fall in-love again. Rebuild trust. Feel desire.</p>

  <div class="abs rank-band">
    <div class="stars">★★★★★</div>
    <p class="rank-text">Podwave Rank : Top 10 in Sexuality Podcasts<br>&amp; Top 5 Couples Therapy Podcasts</p>
  </div>
  <div class="abs subscribe subscribe--front">SUBSCRIBE NOW!</div>

  <div class="abs host host--denise">
    <div class="host-photo host-photo--denise" role="img" aria-label="Portrait of co-host Denise Harlow"></div>
    <p class="host-name">Denise Harlow, LMFT</p>
    <p class="host-role">Certified Sex Therapist</p>
  </div>
  <div class="abs host host--walter">
    <div class="host-photo host-photo--walter" role="img" aria-label="Portrait of co-host Walter Brennick"></div>
    <p class="host-name">Walter Brennick</p>
    <p class="host-role">EFT Trainer/Supervisor</p>
  </div>

  <div class="abs site-band">www.QuillbendAudioHour.com</div>
</section>

<section class="flyer flyer--back">
  <h2 class="abs title title--back">Quillbend - Couples &amp; Sex Therapy</h2>
  <div class="abs rule rule--back"></div>
  <p class="abs tagline tagline--back">Helping couples keep it hot!</p>

  <div class="abs story">
    <p>Our podcast QUILLBEND - Radio Couples and Sex Therapy podcast is for people who want to have hot sex and intimacy with one person - their spouse/partner. Unfortunately, sex is not as naturally easy as we thought. Couples often get into a bind where one person needs emotional connection before they desire sex and the other needs sex in order to be emotionally vulnerable. Then, we grow up thinking that if people really loved each other, they would just get along. No one told us relationship could to get off track seemingly so easily. Many of us didn't have families who talked about emotions much less sex. Without guidance, once you're in the negative cycle of blaming and withdrawing it can feel hope-less. Perhaps you've even worried that you married the wrong person.</p>
    <p>Cohosts Denise Harlow and Walter Brennick are expert therapists who have helped thousands of couples to get back on track both sexually and emotionally with each other. They can help you figure out how your reactions might make sense but why they are pushing your partner away from your heart or out of your bed.</p>
  </div>

  <h3 class="abs topics-heading">WE TALK ABOUT:</h3>
  <ul class="abs topics">
    <li>Frequency differences</li><li>Premature ejaculation</li>
    <li>Low libido</li><li>Men and vulnerability</li>
    <li>Love as the true adventure</li><li>A safe haven relationship</li>
    <li>Her orgasm</li><li>Oral sex</li>
    <li>Pursuer-withdrawer dynamics</li><li>Speaking from the heart</li>
    <li>Erectile dysfunction</li><li>Emotional closeness</li>
  </ul>

  <div class="abs rank-back">
    <div class="stars">★★★★★</div>
    <p class="rank-text">Podwave Rank : Top 10 in Sexuality Podcasts<br>&amp; Top 5 Couples Therapy Podcasts</p>
  </div>

  <svg class="abs base-wave" viewBox="0 0 438 177" aria-hidden="true">
    <path d="M0,38 Q190,70 438,10 L438,177 L0,177 Z" fill="var(--red)"/>
    <path d="M0,50 Q190,84 438,24 L438,177 L0,177 Z" fill="var(--black)"/>
  </svg>
  <div class="abs brand-badge brand-badge--back"><span class="brand-name">QUILLBEND</span></div>
  <div class="abs subscribe subscribe--back">SUBSCRIBE NOW!</div>
  <p class="abs platforms">Found on Podwave, Castline,<br>Tunebox, Streamly and Airdial</p>
</section>

</body>
</html>
```